Business cards design for T38 (Разработка визитных карточек)

We would like to get design of our business cards loosely based on our website design [url removed, login to view]

logo in vector is atteched

There should be following info to be present on business card:
Martin Colvey
CEO
T38
+7 (222) 222-22-22
+7 (222) 222-22-22
colvey@tessarine-mail.ru
222222, Moscow, Ulitsa Tikhvoronskaya, 7B

```html
<!DOCTYPE html>
<html lang="en">
<head>
<meta charset="utf-8">
<title>T38 business cards</title>
<link href="https://fonts.googleapis.com/css2?family=Open+Sans:wght@400;600;800&display=swap" rel="stylesheet">
<style>
  :root {
    --stage: #3a3a3a;
    --stage-dark: #1c1c1c;
    --red: #d0141b;
    --red-dark: #a50e13;
    --white: #f6f6f6;
    --grey-text: #8a8a8a;
    --emblem-fill: #cfcfcf;
  }
  * { box-sizing: border-box; margin: 0; padding: 0; }
  html, body { width: 1197px; height: 1200px; overflow: hidden; }
  body {
    background: radial-gradient(circle at 30% 20%, var(--stage), var(--stage-dark));
    font-family: "Open Sans", Arial, sans-serif;
    position: relative;
  }
  .card {
    position: absolute;
    left: 158px;
    width: 880px;
    height: 500px;
    border-radius: 6px;
    overflow: hidden;
    box-shadow: 0 18px 40px rgba(0,0,0,.45);
  }
  /* back side */
  .card--back { top: 70px; background: var(--red); }
  .back-shapes { position: absolute; inset: 0; }
  .back-logo {
    position: absolute;
    left: 0; right: 0; top: 170px;
    text-align: center;
    color: var(--white);
  }
  .back-logo__name {
    font-weight: 800;
    font-size: 120px;
    line-height: 1;
    letter-spacing: 6px;
  }
  .back-logo__rule {
    width: 300px; height: 3px; margin: 10px auto 8px;
    background: var(--white);
  }
  .back-logo__web { font-size: 22px; letter-spacing: 2px; font-weight: 600; }

  /* front side */
  .card--front { top: 630px; background: var(--red); }
  .front-shapes { position: absolute; inset: 0; }
  .emblem-name {
    position: absolute;
    left: 70px; top: 160px;
    width: 240px;
    text-align: center;
    font-weight: 800;
    font-size: 58px;
    line-height: 80px;
    color: var(--red);
    letter-spacing: 2px;
  }
  .contact {
    position: absolute;
    right: 40px;
    text-align: right;
    color: var(--red);
  }
  .contact__name { top: 34px; font-size: 24px; font-weight: 600; letter-spacing: 1px; }
  .contact__role { top: 66px; font-size: 22px; color: var(--grey-text); }
  .contact__lines { top: 180px; font-size: 22px; line-height: 1.45; letter-spacing: .5px; }
  .contact__lines li { list-style: none; display: flex; justify-content: flex-end; align-items: center; gap: 8px; }
  .contact__lines svg { width: 18px; height: 18px; fill: var(--red); }
  .address {
    position: absolute;
    left: 0; right: 40px; bottom: 28px;
    text-align: right;
    color: var(--white);
    font-size: 26px;
    letter-spacing: 2px;
  }
</style>
</head>
<body>

<section class="card card--back">
  <svg class="back-shapes" viewBox="0 0 880 500" aria-hidden="true">
    <rect width="880" height="500" fill="var(--red)"/>
    <polygon points="0,0 260,0 0,180" fill="var(--red-dark)"/>
    <polygon points="880,0 640,0 880,200" fill="var(--red-dark)"/>
    <polygon points="0,500 0,330 220,500" fill="var(--red-dark)"/>
    <polygon points="880,500 880,320 660,500" fill="var(--red-dark)"/>
  </svg>
  <div class="back-logo">
    <div class="back-logo__name">T38</div>
    <div class="back-logo__rule"></div>
    <div class="back-logo__web">www.tessarine-t38.ru</div>
  </div>
</section>

<section class="card card--front">
  <svg class="front-shapes" viewBox="0 0 880 500">
    <rect width="880" height="500" fill="var(--red)"/>
    <path d="M300 0 H880 V395 H330 C410 330 420 200 360 110 C340 70 320 35 300 0 Z" fill="var(--white)"/>
    <circle cx="190" cy="200" r="140" fill="var(--emblem-fill)" role="img" aria-label="Emblem area behind the company name"/>
  </svg>
  <div class="emblem-name">T38</div>
  <div class="contact contact__name">Martin Colvey</div>
  <div class="contact contact__role">CEO, T38</div>
  <ul class="contact contact__lines">
    <li>+7 (222) 222-22-22
      <svg viewBox="0 0 24 24"><path d="M6.6 10.8a15 15 0 0 0 6.6 6.6l2.2-2.2a1 1 0 0 1 1-.25 11.4 11.4 0 0 0 3.6.6 1 1 0 0 1 1 1V20a1 1 0 0 1-1 1A17 17 0 0 1 3 4a1 1 0 0 1 1-1h3.5a1 1 0 0 1 1 1c0 1.250.2 2.450.6 3.6a1 1 0 0 1-.25 1z"/></svg></li>
    <li>+7 (222) 222-22-22
      <svg viewBox="0 0 24 24"><path d="M7 1h10a2 2 0 0 1 2 2v18a2 2 0 0 1-2 2H7a2 2 0 0 1-2-2V3a2 2 0 0 1 2-2zm0 3v14h10V4z"/></svg></li>
    <li>colvey@tessarine-mail.ru
      <svg viewBox="0 0 24 24"><path d="M2 5h20v14H2zm2 2v.5l8 5 8-5V7l-8 5z"/></svg></li>
  </ul>
  <div class="address">222222, Moscow, Ulitsa Tikhvoronskaya, 7B</div>
</section>

</body>
</html>
```